We need a logo and landing page designed. We are a full-service general contractor based in Tempe Arizona. We can provide all phases of construction from design to completion. We specialize in commercial and residential remodels, as well as ground-up construction. We will like to see designs that primarily used reds, blues, blacks, whites, etc. The design should be a professional yet fun, easy-to-read format. Our name is Oak Ledger Construction...I would like to see some designs that incorporate a "oak ledger" and some without.
The final design should communicate a professional, quality-driven, safety oriented full service business.

Target Market(s)

Building owners, land developers, homeowners

Industry/Entity Type

Commercial Construction

Coding

Coded - Design and coding required

Number of Pages Required

1 page

Font styles to use
Serif

Colors
0054AA
0677BA
7BADD7
CADEEF
E8F1F8
59FF00
82FF00
B8FF75
E3FFCB
F4FFEA
EE7325
F08F49
F5BC92
FAE3D3
FDF4ED
EB3D1F
EC4F4E
F09395
F8D3D4
FCEDEE

```html
<!DOCTYPE html>
<html lang="en">
<head>
<meta charset="utf-8">
<title>Oak Ledger Construction</title>
<link href="https://fonts.googleapis.com/css2?family=Montserrat:wght@600;700;800;900&family=Open+Sans:ital,wght@0,400;0,600;0,700;1,400&display=swap" rel="stylesheet">
<style>
:root{
  --red:#EB3D1F;
  --red-soft:#EC4F4E;
  --blue:#0054AA;
  --blue-mid:#0677BA;
  --orange:#EE7325;
  --green:#59FF00;
  --ink:#161616;
  --text:#555;
  --white:#fff;
  --hero-bg:#eef0f1;
}
*{margin:0;padding:0;box-sizing:border-box}
html,body{width:1200px;height:3495px;overflow:hidden}
body{position:relative;background:var(--white);font-family:"Open Sans",Arial,sans-serif;color:var(--ink)}
.abs{position:absolute}
.head-font{font-family:"Montserrat",Arial,sans-serif}

/* header */
.site-header{position:absolute;left:0;top:0;width:1200px;height:75px;background:var(--white);box-shadow:0 2px 6px rgba(0,0,0,.08);z-index:5}
.brand{position:absolute;left:60px;top:16px;font-family:"Montserrat",sans-serif;font-weight:800;color:var(--red);font-size:19px;line-height:21px;letter-spacing:.5px}
.brand small{display:block;font-size:11px;letter-spacing:1.6px;line-height:14px;font-weight:800}
.main-nav{position:absolute;left:622px;top:30px;display:flex;gap:21px;font-size:12.5px;color:#333}
.main-nav .active{color:var(--red);border-bottom:1.5px solid var(--red);padding-bottom:5px}
.phone-box{position:absolute;left:982px;top:18px;width:158px;height:38px;border:2px solid var(--red);color:var(--red);font-family:"Montserrat",sans-serif;font-weight:700;font-size:16px;display:flex;align-items:center;justify-content:center;gap:8px}

/* hero */
.hero{position:absolute;left:0;top:75px;width:1200px;height:680px;background:linear-gradient(180deg,#e9ebec 0%,#f3f4f5 70%,#fff 100%)}
.hero-title{position:absolute;left:58px;top:250px;font-family:"Montserrat",sans-serif;font-weight:900;font-size:57px;line-height:60px;letter-spacing:.5px}
.hero-title span{color:var(--red);display:block}
.hero-sub{position:absolute;left:61px;top:380px;font-style:italic;font-size:16px;line-height:25px;color:#333}
.btn-blue{position:absolute;left:61px;top:450px;width:143px;height:41px;background:var(--blue);color:#fff;font-family:"Montserrat",sans-serif;font-weight:700;font-size:15px;display:flex;align-items:center;justify-content:center}
.hero-art{position:absolute;left:0;top:0}

/* sections */
.section-title{position:absolute;left:0;width:1200px;text-align:center;font-family:"Montserrat",sans-serif;font-weight:800;font-size:33px;letter-spacing:-.5px}
.section-title span,.red{color:var(--red)}
.kicker{position:absolute;font-size:15px;color:#222}
.italic-sub{position:absolute;left:0;width:1200px;text-align:center;font-style:italic;font-size:13.5px;line-height:20px;color:#444}
.read-more{position:absolute;font-weight:700;font-size:14px;color:var(--blue);display:flex;align-items:center;gap:8px}

.service-card{position:absolute;top:988px;width:284px;height:313px;border:1.5px solid;border-radius:10px;background:#fff}
.service-card h3{position:absolute;top:128px;left:0;width:100%;text-align:center;font-family:"Montserrat",sans-serif;font-weight:700;font-size:17px;line-height:24px}
.service-card p{position:absolute;top:188px;left:30px;width:224px;text-align:center;font-size:12.5px;line-height:19.5px;color:var(--text)}
.service-card .read-more{top:263px;left:0;width:100%;justify-content:center}
.svc-hex{position:absolute;top:-74px;left:67px}

/* about */
.years-box{position:absolute;left:117px;top:1411px;width:89px;height:72px;background:var(--orange)}
.years-num{position:absolute;left:138px;top:1408px;font-family:"Montserrat",sans-serif;font-weight:800;font-size:62px;line-height:76px}
.years-label{position:absolute;left:139px;top:1493px;font-family:"Montserrat",sans-serif;font-weight:700;font-size:14px;line-height:20px}
.about-title{position:absolute;left:334px;top:1410px;font-family:"Montserrat",sans-serif;font-weight:800;font-size:31px;line-height:38px}
.about-sub{position:absolute;left:335px;top:1492px;font-style:italic;font-size:13.5px;line-height:21px;color:var(--red)}
.about-body{position:absolute;left:335px;top:1548px;width:350px;font-size:12.5px;line-height:21px;color:var(--text)}
.about-body p+p{margin-top:10px}

/* projects */
.project{position:absolute;width:432px;height:225px;border-radius:12px;overflow:hidden}
.project-label{position:absolute;left:0;bottom:22px;height:44px;padding:0 20px;display:flex;align-items:center;background:rgba(0,0,0,.45);color:#fff;font-family:"Montserrat",sans-serif;font-weight:700;font-size:16px}

/* news */
.news-box{position:absolute;left:136px;top:2698px;width:522px;height:292px;border:1.5px solid var(--orange);background:#fff}
.news-date{position:absolute;left:36px;top:53px;width:106px;height:31px;background:var(--red);color:#fff;font-size:12px;font-weight:700;display:flex;align-items:center;justify-content:center}
.news-title{position:absolute;left:36px;top:103px;font-family:"Montserrat",sans-serif;font-weight:700;font-size:15px}
.news-text{position:absolute;left:36px;top:134px;width:340px;font-size:11.5px;line-height:20.5px;color:var(--text)}
.news-box .read-more{left:38px;top:225px}

/* footer */
.footer-h{position:absolute;top:3221px;font-family:"Montserrat",sans-serif;font-weight:800;font-size:15px;color:#fff}
.footer-list{position:absolute;top:3258px;list-style:none;font-size:11.5px;color:#fff}
.footer-list li{height:24px;display:flex;align-items:center;gap:13px}
.footer-list li::before{content:"";width:6px;height:6px;border-radius:50%;background:var(--orange)}
.contact-line{position:absolute;left:519px;font-size:11.5px;line-height:18px;color:#fff}
.contact-icon{position:absolute;left:486px}
.contact-title{position:absolute;left:747px;width:453px;top:3128px;text-align:center;font-family:"Montserrat",sans-serif;font-weight:800;font-size:31px;color:#fff}
.contact-sub{position:absolute;left:747px;width:453px;top:3172px;text-align:center;font-style:italic;font-size:13px;color:#fff}
.field{position:absolute;left:825px;width:315px;height:30px;background:#fff;font-size:11.5px;color:#777;padding:8px 12px}
.submit{position:absolute;left:825px;top:3420px;width:92px;height:39px;background:var(--blue);color:#fff;font-family:"Montserrat",sans-serif;font-weight:800;font-size:15px;display:flex;align-items:center;justify-content:center}
.copyright{position:absolute;left:61px;top:3458px;font-size:11px;color:#fff}
</style>
</head>
<body>

<header class="site-header">
  <div class="brand">OAK LEDGER<small>CONSTRUCTION</small></div>
  <nav class="main-nav">
    <span class="active">HOME</span><span>SERVICES</span><span>PROJECTS</span><span>NEWS</span><span>CONTACT US</span>
  </nav>
  <div class="phone-box">
    <svg width="18" height="18" viewBox="0 0 24 24" fill="none" stroke="currentColor" stroke-width="2"><path d="M5 3h4l2 5-2.5 1.5a11 11 0 0 0 6 6L16 13l5 2v4a2 2 0 0 1-2 2A17 17 0 0 1 3 5a2 2 0 0 1 2-2z"/></svg>
    555.014.2280
  </div>
</header>

<section class="hero">
  <svg class="hero-art" width="1200" height="680" viewBox="0 0 1200 680">
    <polygon points="616,140 616,495 937,680 1200,525 1200,0 690,0" fill="var(--blue)"/>
    <polygon points="648,110 690,0 1200,0 1200,505 937,625 648,460" fill="#c8956a" role="img" aria-label="Wood-framed multi-storey building under construction against a blue sky"/>
    <polygon points="648,110 690,0 1200,0 1200,160 648,160" fill="#8fb4d8" opacity=".7"/>
    <line x1="60" y1="548" x2="147" y2="548" stroke="var(--red)" stroke-width="1.2"/>
    <polygon points="173,537 192,527 211,537 211,559 192,569 173,559" fill="#fff" stroke="var(--red)" stroke-width="1.2"/>
    <polyline points="196,541 189,548 196,555" fill="none" stroke="var(--red)" stroke-width="2"/>
    <polygon points="199,537 218,527 237,537 237,559 218,569 199,559" fill="var(--red)"/>
    <polyline points="214,541 221,548 214,555" fill="none" stroke="#fff" stroke-width="2"/>
  </svg>
  <h1 class="hero-title" style="top:175px">GROUND-UP<span>CONSTRUCTION.</span></h1>
  <p class="hero-sub" style="top:305px">We Specialize In Commercial And Residential Remodels,<br>As Well As Ground-Up Construction</p>
  <div class="btn-blue" style="top:375px">CONTACT US</div>
</section>

<h2 class="section-title" style="top:780px"><span>OUR</span> SERVICES</h2>
<p class="italic-sub" style="top:830px">We Specialize In Commercial And Residential Remodels, As Well As<br>Ground-Up Construction</p>

<div class="service-card" style="left:161px;border-color:var(--blue)">
  <svg class="svc-hex" width="150" height="172" viewBox="0 0 150 172"><polygon points="75,2 148,44 148,128 75,170 2,128 2,44" fill="var(--blue)"/><polygon points="80,0 150,40 150,126 80,166 8,124 8,40" fill="#b9c7d6" role="img" aria-label="Curved white modern architecture building"/></svg>
  <h3>ARCHITECTURE &amp;<br>BUILDING</h3>
  <p>Lorem Ipsum has been the industry's standard text ever since the, when an unknown been industry</p>
  <div class="read-more">Read More <svg width="28" height="8" viewBox="0 0 28 8"><path d="M0 4h24M20 1l4 3-4 3" stroke="var(--blue)" fill="none" stroke-width="1.3"/></svg></div>
</div>
<div class="service-card" style="left:468px;border-color:var(--green)">
  <svg class="svc-hex" width="150" height="172" viewBox="0 0 150 172"><polygon points="75,2 148,44 148,128 75,170 2,128 2,44" fill="var(--green)"/><polygon points="70,0 142,40 142,126 70,166 0,124 0,40" fill="#9aa7a8" role="img" aria-label="Construction consultants in hard hats on site"/></svg>
  <h3>CONSTRUCTION<br>CONSULTANTS</h3>
  <p>Lorem Ipsum has been the industry's standard text ever since the, when an unknown been industry</p>
  <div class="read-more">Read More <svg width="28" height="8" viewBox="0 0 28 8"><path d="M0 4h24M20 1l4 3-4 3" stroke="var(--blue)" fill="none" stroke-width="1.3"/></svg></div>
</div>
<div class="service-card" style="left:776px;border-color:var(--orange)">
  <svg class="svc-hex" width="150" height="172" viewBox="0 0 150 172"><polygon points="75,2 148,44 148,128 75,170 2,128 2,44" fill="var(--orange)"/><polygon points="78,0 150,40 150,122 78,162 6,122 6,40" fill="#8da7c4" role="img" aria-label="Construction managers reviewing a timber frame"/></svg>
  <h3>CONSTRUCTION<br>MANAGEMENT</h3>
  <p>Lorem Ipsum has been the industry's standard text ever since the, when an unknown been industry</p>
  <div class="read-more">Read More <svg width="28" height="8" viewBox="0 0 28 8"><path d="M0 4h24M20 1l4 3-4 3" stroke="var(--blue)" fill="none" stroke-width="1.3"/></svg></div>
</div>

<div class="years-box"></div>
<div class="years-num">05+</div>
<div class="years-label">YEAR OF<br>EXPERIENCE</div>
<div class="kicker" style="left:336px;top:1382px">About</div>
<h2 class="about-title"><span class="red">OAK LEDGER</span><br>CONSTRUCTION</h2>
<p class="about-sub">We Specialize In Commercial And Residential Remodels,<br>As Well As Ground-Up Construction</p>
<div class="about-body">
  <p>Lorem Ipsum has been the industry's standard dummy text ever since the 1500s, when an unknown printer took a galley of type and scrambled it to make a type specimen</p>
  <p>Lorem Ipsum has been the industry's standard dummy text ever since the , when an unknown printer took.</p>
</div>
<div class="read-more" style="left:335px;top:1681px">Read More <svg width="28" height="8" viewBox="0 0 28 8"><path d="M0 4h24M20 1l4 3-4 3" stroke="var(--blue)" fill="none" stroke-width="1.3"/></svg></div>
<div class="abs" style="left:765px;top:1384px;width:435px;height:346px;background:linear-gradient(90deg,#8d7a66 0%,#8d7a66 50%,#dcd6cf 50%,#ece8e2 100%)" role="img" aria-label="Room interior shown before and after renovation"></div>

<div class="kicker" style="left:0;width:1200px;text-align:center;top:1810px">Our Works</div>
<h2 class="section-title" style="top:1835px"><span>OUR</span> PROJECTS</h2>

<div class="project" style="left:157px;top:1916px;background:linear-gradient(135deg,#3a3a3a,#b9b7b2 60%,#d8d6d2)" role="img" aria-label="Modern office reception interior"><div class="project-label">ARCHITECTURE</div></div>
<div class="project" style="left:611px;top:1916px;background:linear-gradient(135deg,#e86a52,#e2553c)" role="img" aria-label="Dining room interior with red overlay">
  <svg class="abs" style="left:187px;top:84px" width="58" height="58" viewBox="0 0 58 58"><circle cx="29" cy="29" r="27" fill="none" stroke="#fff" stroke-width="1.5"/><path d="M29 12v34M12 29h34" stroke="#fff" stroke-width="1.5"/></svg>
</div>
<div class="project" style="left:157px;top:2171px;background:linear-gradient(180deg,#c9d2d8,#9c8a76 55%,#5f6b4e)" role="img" aria-label="Single-storey family house with porch"><div class="project-label">RESIDENTIAL</div></div>
<div class="project" style="left:611px;top:2171px;background:linear-gradient(180deg,#cfd3d6,#6b6f74 60%,#3d4045)" role="img" aria-label="Modern commercial apartment building"><div class="project-label">COMMERCIAL</div></div>

<div class="read-more" style="left:546px;top:2431px">Explore All <svg width="28" height="8" viewBox="0 0 28 8"><path d="M0 4h24M20 1l4 3-4 3" stroke="var(--blue)" fill="none" stroke-width="1.3"/></svg></div>

<div class="kicker" style="left:140px;top:2584px">Stay Updated</div>
<h2 class="section-title" style="left:138px;width:auto;top:2613px;text-align:left"><span>LATEST</span> NEWS</h2>
<div class="abs" style="left:562px;top:2547px;width:503px;height:375px;background:linear-gradient(135deg,#3b3b3b,#c9cfd6 45%,#e6e8ea)" role="img" aria-label="Two engineers in yellow hard hats reading construction plans"></div>
<div class="news-box">
  <div class="news-date">14 April 2022</div>
  <div class="news-title">LOREM IPSUM INDUSTRY'S PRINT !</div>
  <p class="news-text">Lorem Ipsum has been the industry standard dummy text ever since the, when unknown printer took a galley type scrambled Lorem Ipsum has been the industry standard dummy text ever since the, when unknown printer took a galley..</p>
  <div class="read-more">Read More <svg width="28" height="8" viewBox="0 0 28 8"><path d="M0 4h24M20 1l4 3-4 3" stroke="var(--blue)" fill="none" stroke-width="1.3"/></svg></div>
</div>

<svg class="abs" style="left:0;top:3030px" width="1200" height="465" viewBox="0 0 1200 465">
  <polygon points="0,91 747,145 747,465 0,465" fill="var(--blue)"/>
  <polygon points="747,145 988,4 1200,125 1200,465 747,465" fill="var(--red)"/>
  <line x1="0" y1="406" x2="747" y2="406" stroke="rgba(255,255,255,.25)"/>
</svg>

<div class="footer-h" style="left:61px">SITE MAP</div>
<ul class="footer-list" style="left:61px"><li>About</li><li>Services</li><li>Projects</li><li>News</li><li>Contact</li></ul>
<div class="footer-h" style="left:248px">OUR SERVICES</div>
<ul class="footer-list" style="left:248px"><li>Architecture &amp; Building</li><li>Construction Consultants</li><li>Construction Management</li></ul>
<div class="footer-h" style="left:487px">CONTACT US</div>
<svg class="contact-icon" style="top:3268px" width="18" height="22" viewBox="0 0 18 22"><path d="M9 21s7-7 7-12A7 7 0 0 0 2 9c0 5 7 12 7 12z" fill="none" stroke="var(--orange)" stroke-width="1.4"/><circle cx="9" cy="9" r="2.5" fill="none" stroke="var(--orange)" stroke-width="1.4"/></svg>
<div class="contact-line" style="top:3260px">OAK LEDGER CONSTRUCTION<br>101 - Lorem ipsum simple text<br>print type setting industry !</div>
<svg class="contact-icon" style="top:3330px" width="20" height="20" viewBox="0 0 24 24" fill="none" stroke="var(--orange)" stroke-width="1.6"><path d="M5 3h4l2 5-2.5 1.5a11 11 0 0 0 6 6L16 13l5 2v4a2 2 0 0 1-2 2A17 17 0 0 1 3 5a2 2 0 0 1 2-2z"/></svg>
<div class="contact-line" style="top:3332px;font-weight:700;font-size:13px">1.555.014.2280</div>
<svg class="contact-icon" style="top:3367px" width="20" height="16" viewBox="0 0 20 16"><rect x="1" y="1" width="18" height="14" fill="none" stroke="var(--orange)" stroke-width="1.4"/><path d="M1 1l9 8 9-8" fill="none" stroke="var(--orange)" stroke-width="1.4"/></svg>
<div class="contact-line" style="top:3366px">info@OakLedgerConstruction.com</div>

<div class="contact-title">CONTACT US</div>
<div class="contact-sub">If you have any Question for contact us today !</div>
<div class="field" style="top:3219px">Name *</div>
<div class="field" style="top:3260px">Phone *</div>
<div class="field" style="top:3302px">Email*</div>
<div class="field" style="top:3342px;height:67px">Message *</div>
<div class="submit">SUBMIT</div>

<div class="copyright">©OAK LEDGER CONSTUCTION - 2022 All rights reserved.</div>

</body>
</html>
```